Brightpath Letterhead

We would like a letterhead for our company. I have uploaded our logo.

Brightpath Ridge Consulting
1450 W Corliss Ave Ste 310
Arlington, TX 76006
833-517-2906

```html
<!DOCTYPE html>
<html lang="en">
<head>
<meta charset="utf-8">
<title>Brightpath Ridge Consulting Letterhead</title>
<link rel="stylesheet" href="https://fonts.googleapis.com/css2?family=Montserrat:wght@300;400;700&family=Lato:wght@400&display=swap">
<style>
  :root {
    --teal: #1d5a6b;
    --mint: #5cbf94;
    --ink: #555555;
    --ink-soft: #5e5e5e;
    --paper: #ffffff;
    --sig-tone: #d3e4e8;
  }
  * { margin: 0; padding: 0; box-sizing: border-box; }
  html, body { width: 1056px; height: 1200px; overflow: hidden; background: var(--paper); }
  .letterhead {
    position: relative;
    width: 1056px;
    height: 1200px;
    background: var(--paper);
    font-family: "Lato", sans-serif;
    color: var(--ink);
  }
  .brand {
    position: absolute;
    top: 70px;
    left: 0;
    width: 100%;
    display: flex;
    justify-content: center;
    align-items: center;
    gap: 16px;
  }
  .brand-dot {
    width: 52px; height: 52px; border-radius: 50%;
    background: var(--mint);
  }
  .brand-name {
    font-family: "Montserrat", sans-serif;
    font-weight: 700;
    font-size: 24px;
    line-height: 1.25;
    letter-spacing: 4px;
    text-transform: uppercase;
    color: var(--teal);
  }
  .brand-name span { display: block; }
  .letter-meta {
    position: absolute;
    top: 354px;
    left: 128px;
    font-family: "Montserrat", sans-serif;
  }
  .letter-date { font-weight: 300; font-size: 20px; color: var(--ink-soft); }
  .sender-name { font-weight: 700; font-size: 31px; color: var(--ink); margin-top: 10px; letter-spacing: 0.3px; }
  .sender-title { font-weight: 300; font-size: 21px; color: var(--ink-soft); margin-top: 6px; }
  .letter-body {
    position: absolute;
    top: 510px;
    left: 128px;
    width: 800px;
    font-size: 16.5px;
    line-height: 23px;
    text-align: justify;
  }
  .letter-body p + p { margin-top: 15px; }
  .sign-off {
    position: absolute;
    top: 836px;
    left: 128px;
    font-size: 21px;
    color: var(--ink-soft);
  }
  .signature {
    position: absolute;
    top: 886px;
    left: 128px;
    width: 116px;
    height: 44px;
    background: var(--sig-tone);
    border-radius: 4px;
  }
  .contact-bar {
    position: absolute;
    top: 1138px;
    left: 0;
    width: 100%;
    display: flex;
    justify-content: center;
    align-items: center;
    gap: 26px;
    font-size: 20px;
    color: #3f3f3f;
  }
  .contact-item { display: flex; align-items: center; gap: 14px; }
  .contact-icon { width: 20px; height: 22px; flex: none; }
</style>
</head>
<body>
<main class="letterhead">
  <header class="brand">
    <div class="brand-dot"></div>
    <div class="brand-name"><span>Brightpath Ridge</span><span>Consulting</span></div>
  </header>

  <section class="letter-meta">
    <p class="letter-date">01 December, 2021</p>
    <h1 class="sender-name">DANIEL HARPER</h1>
    <p class="sender-title">Cheif Executive Officer</p>
  </section>

  <section class="letter-body">
    <p>Contrary to popular belief, Lorem Ipsum is not simply random text. It has roots in a piece of classical Latin literature from 45 BC, making it over 2000 years old. Howard Bellamy, a Latin professor at Harlow Creek College in Virginia, looked up one of the more obscure Latin words, consectetur. The standard chunk of Lorem Ipsum used since the 1500s is reproduced below for those interested.</p>
    <p>Lorem Ipsum comes from sections 1.10.32 and 1.10.33 of "de Finibus Bonorum et Malorum" (The Extremes of Good and Evil) by Aulus Fenn, written in 45 BC. This book is a treatise on the theory of ethics, very popular during the Renaissance. The first line of Lorem Ipsum.This book is a treatise on the theory of ethics, very popular during the Renaissance. The first line of Lorem Ipsum.</p>
    <p>The standard chunk of Lorem Ipsum used since the 1500s is reproduced below for those interested. This book is a treatise on the theory of ethics, very popular during the Renaissance. The first line of Lorem Ipsum. The first line of Lorem Ipsum.This book is a treatise on the theory of ethics, very popular during the Renaissance.</p>
  </section>

  <p class="sign-off">Best Regards</p>
  <div class="signature" role="img" aria-label="Handwritten signature of Daniel Harper"></div>

  <footer class="contact-bar">
    <div class="contact-item">
      <svg class="contact-icon" viewBox="0 0 20 22" aria-hidden="true">
        <path d="M10 1a7 7 0 0 0-7 7c0 5 7 13 7 13s7-8 7-13a7 7 0 0 0-7-7z" fill="var(--mint)"/>
        <circle cx="10" cy="8" r="2.6" fill="#fff"/>
      </svg>
      <span>1450 W Corliss Ave Ste 310 Arlington, TX 76006</span>
    </div>
    <div class="contact-item">
      <svg class="contact-icon" viewBox="0 0 22 22" aria-hidden="true">
        <path d="M5 3l3 0 1.5 4-2 1.5a11 11 0 0 0 6 6l1.5-2 4 1.5v3a2 2 0 0 1-2 2A16 16 0 0 1 3 5a2 2 0 0 1 2-2z" fill="none" stroke="var(--mint)" stroke-width="1.8" stroke-linejoin="round"/>
        <path d="M13 2.5a7 7 0 0 1 6.5 6.5M13 6a3.5 3.5 0 0 1 3 3" fill="none" stroke="var(--mint)" stroke-width="1.6" stroke-linecap="round"/>
      </svg>
      <span>833-517-2906</span>
    </div>
  </footer>
</main>
</body>
</html>
```